Business card design needed

We are a wine business involved in winemaking, broking and packaging on behalf of clients globally with the majority being Asian. The design should be quite traditional and classic with some red used, font used should be easily read.

Target Market(s)

Trade customers other business owners

Industry/Entity Type

Business

Contact Information for Business Card

Rosalind Thwaite
Meridale Wine Collective
PO Box 738, Fenwick Vale
South Australia 5187
Phone: +61 (0)455 982 317
Email: kvcellars@brightmail.example

Logo styles of interest
Lettermark Logo

```html
<!DOCTYPE html>
<html lang="en">
<head>
<meta charset="utf-8">
<title>Rosalind Thwaite – Business Card</title>
<link rel="stylesheet" href="https://fonts.googleapis.com/css2?family=Sawarabi+Mincho&family=Crimson+Pro:wght@500&display=swap">
<style>
  :root {
    --backdrop: #d8d6d2;
    --card-edge: #8a8d88;
    --card-light: #3c3c41;
    --card-mid: #1c1c1f;
    --card-dark: #000000;
    --name-grey: #b8b8bc;
    --company-grey: #c9c9cd;
    --wine-red: #a5282c;
    --rule-red: #8e2a2c;
    --contact-white: #ececec;
  }
  * { margin: 0; padding: 0; box-sizing: border-box; }
  html, body {
    width: 1200px;
    height: 1000px;
    overflow: hidden;
    background: var(--backdrop);
  }
  .card {
    position: absolute;
    left: 165px;
    top: 250px;
    width: 870px;
    height: 500px;
    border: 4px solid var(--card-edge);
    background: radial-gradient(ellipse 620px 520px at 170px 250px,
      var(--card-light) 0%, var(--card-mid) 55%, var(--card-dark) 100%);
  }
  .brand {
    position: absolute;
    left: 44px;
    top: 226px;
    display: flex;
    align-items: center;
    gap: 12px;
  }
  .brand-square {
    width: 14px;
    height: 14px;
    background: var(--wine-red);
  }
  .brand-name {
    font-family: "Sawarabi Mincho", serif;
    font-size: 18px;
    color: var(--wine-red);
    white-space: nowrap;
  }
  .identity {
    position: absolute;
    left: 383px;
    top: 170px;
    width: 358px;
    text-align: center;
  }
  .person-name {
    font-family: "Sawarabi Mincho", serif;
    font-weight: 400;
    font-size: 36px;
    letter-spacing: 1px;
    color: var(--name-grey);
    line-height: 50px;
  }
  .rule {
    height: 1px;
    background: var(--rule-red);
    margin-top: 12px;
  }
  .company {
    font-family: "Sawarabi Mincho", serif;
    font-size: 17px;
    letter-spacing: 0.5px;
    text-transform: uppercase;
    color: var(--company-grey);
    margin-top: 17px;
  }
  .stars {
    display: block;
    margin: 16px auto 0;
  }
  .contact {
    position: absolute;
    left: 571px;
    top: 341px;
    list-style: none;
    font-family: "Crimson Pro", serif;
    font-weight: 500;
    font-size: 15.5px;
    color: var(--contact-white);
    line-height: 29.5px;
  }
</style>
</head>
<body>
  <div class="card">
    <div class="brand">
      <span class="brand-square"></span>
      <span class="brand-name">Meridale Wine Collective</span>
    </div>

    <div class="identity">
      <h1 class="person-name">Rosalind Thwaite</h1>
      <div class="rule"></div>
      <p class="company">Meridale Wine Collective</p>
      <svg class="stars" width="200" height="18" viewBox="0 0 200 18" aria-hidden="true">
        <defs>
          <polygon id="star" points="9,0 11.1,6.2 17.6,6.2 12.4,10.1 14.3,16.4 9,12.6 3.7,16.4 5.6,10.1 0.4,6.2 6.9,6.2" fill="#a5282c"/>
        </defs>
        <use href="#star" x="0"/>
        <use href="#star" x="45"/>
        <use href="#star" x="91"/>
        <use href="#star" x="136"/>
        <use href="#star" x="182"/>
      </svg>
    </div>

    <ul class="contact">
      <li>PO Box 738, Fenwick Vale</li>
      <li>South Australia 5187</li>
      <li>Phone: +61 (0)455 982 317</li>
      <li>Email: kvcellars@brightmail.example</li>
    </ul>
  </div>
</body>
</html>
```